New Consulting Firm News PowerPoint Template

We are a new consulting firm that specializes in Veltrix Unified Results Planning implementations in need of a new PowerPoint template. We need at least the following layouts:
• Main Cover Slide
• Agenda / Table of Contents
• Title slide for each of the agenda items leading into actual content
• Title + Content with nice bullets in the content
• Title + Sub-Title + Content with nice bullets in the content
• Title + Two Columns of Content
• Title + Sub-Title + Two Columns of Content
• Title + Three Columns of Content
• Title + Sub-Title + Three Columns of Content
• Title + Two Rows and Two Columns of Content (4 boxes)
• Title + Sub-Title + Two Rows and Two Columns of Content (4 boxes)
• Title + Blank
• Nascar Slide (Client logos arranged somehow)
• Case Study Slide
• Various infographic slides than can be used and modified would be amazing as well
Our logo has been uploaded and you can find our website here:
https://brankelladvisory.example
We would like the main theme colors to blend with our logo, but also have a variety of colors in the theme that compliment the main theme colors. Once we have selected a PowerPoint design we expect to immediately have a Word design contest and the winning PowerPoint design will likely be a heavy influence on the Word design.

Target Market(s)

CFO, CAO, VP of Finance, Controllers

Industry/Entity Type

Consulting

Font styles to use
Serif
Sans Serif

Requirements
Must have
• • Main Cover Slide
• Title + Blank
• Case Study Slide
Nice to have
• • Various infographic slides than can be used and modified would be amazing as well

```html
<!DOCTYPE html>
<html lang="en">
<head>
<meta charset="utf-8">
<title>Brankell Advisory – Presentation Template</title>
<link href="https://fonts.googleapis.com/css2?family=Montserrat:wght@400;500;600;700&display=swap" rel="stylesheet">
<style>
  :root{
    --board:#121212;
    --blue:#1e5dbf;
    --blue-deep:#1848a3;
    --blue-light:#2f78d8;
    --grey-bg:#cdcdcd;
    --grey-col:#bdbdbd;
    --grey-row:#d9d9d9;
    --ink:#555555;
    --ink-dark:#1f1f1f;
    --white:#ffffff;
    --tab:#222222;
  }
  *{box-sizing:border-box;margin:0;padding:0}
  html,body{width:1200px;height:1020px;overflow:hidden;background:var(--board)}
  body{font-family:"Montserrat",sans-serif}
  .board{position:relative;width:1200px;height:1020px;background:var(--board)}
  .slide{position:absolute;width:576px;height:324px;overflow:hidden}
  .slide--cover{left:18px;top:15px;background:var(--white)}
  .slide--agenda{left:18px;top:351px}
  .slide--section{left:18px;top:687px;background:var(--grey-bg)}
  .slide--bullets{left:606px;top:9px}
  .slide--subtitle{left:606px;top:351px;background:var(--grey-bg)}
  .slide--columns{left:606px;top:687px}
  .bg-blue{background:radial-gradient(ellipse at 35% 35%,var(--blue-light) 0%,var(--blue) 45%,var(--blue-deep) 100%)}
  .shapes{position:absolute;inset:0;width:100%;height:100%}
  .tab{position:absolute;right:10px;top:0;width:22px;height:22px;background:var(--tab);
       clip-path:polygon(0 0,100% 0,100% 80%,50% 100%,0 80%);color:var(--white);
       font-size:8px;text-align:center;line-height:19px;font-weight:500}
  .tab--blue{background:var(--blue)}
  .brand{position:absolute;left:0;top:8px;width:92px;text-align:center;color:var(--blue);font-weight:600}
  .brand__mark{display:block;width:16px;height:16px;margin:0 auto 4px;background:var(--blue)}
  .brand__name{font-size:8.5px;line-height:10px;letter-spacing:.5px;text-transform:uppercase}
  /* cover */
  .cover-brand{position:absolute;left:20px;top:30px;width:250px;text-align:center;color:var(--blue);font-weight:600}
  .cover-brand__mark{display:block;width:70px;height:70px;margin:0 auto 22px;background:var(--blue)}
  .cover-brand__name{font-size:36px;line-height:40px;letter-spacing:2px}
  .cover-brand__sub{font-size:15px;letter-spacing:6px;margin-top:2px}
  .cover-title{position:absolute;left:7px;top:240px;color:var(--ink);font-weight:700;font-size:27.5px;line-height:33px;text-transform:uppercase}
  /* headings */
  .heading{position:absolute;font-weight:700;font-size:23px;line-height:25px;text-transform:uppercase}
  .heading--white{color:var(--white)}
  .heading--blue{color:var(--blue)}
  /* agenda */
  .agenda-title{left:0;width:576px;text-align:center;top:7px}
  .agenda-table{position:absolute;left:102px;top:41px;width:464px;border-collapse:collapse;font-size:7.5px;color:var(--ink-dark)}
  .agenda-table th{background:var(--ink-dark);color:var(--white);font-size:11.5px;font-weight:600;text-align:left;height:29px;padding-left:11px}
  .agenda-table th:first-child{padding-left:8px}
  .agenda-table td{height:24.3px;border-bottom:1px solid var(--blue);padding-left:11px;background:var(--grey-row)}
  .agenda-table td.pg{width:56px;background:var(--grey-col);text-align:center;padding-left:0}
  .agenda-table tr:last-child td{border-bottom:none}
  /* text */
  .body-copy{position:absolute;font-size:6.3px;line-height:12px;color:var(--ink)}
  .body-copy p{margin-bottom:12px}
  .bullets{position:absolute;list-style:none;font-size:7.5px}
  .bullets li{position:relative;padding-left:8px;height:21px}
  .bullets li::before{content:"";position:absolute;left:0;top:3.5px;width:2.5px;height:2.5px;border-radius:50%;background:currentColor}
  .bullets--white{color:var(--white)}
  .bullets--dark{color:var(--ink-dark)}
  .subtitle{position:absolute;font-size:9px;line-height:15px;font-weight:600;color:var(--ink-dark)}
  .column{position:absolute;top:135px;width:270px;font-size:7.3px;line-height:14.4px;color:var(--white)}
  .column p{margin-bottom:14.4px}
</style>
</head>
<body>
<div class="board">

  <!-- 1 cover -->
  <section class="slide slide--cover">
    <svg class="shapes" viewBox="0 0 576 324" preserveAspectRatio="none">
      <defs>
        <linearGradient id="coverPhoto" x1="0" y1="0" x2="1" y2="1">
          <stop offset="0" stop-color="#3b2d7a"/>
          <stop offset=".5" stop-color="#1f2850"/>
          <stop offset="1" stop-color="#2a4a8c"/>
        </linearGradient>
      </defs>
      <polygon points="297,0 576,0 576,322 297,163" fill="url(#coverPhoto)" role="img" aria-label="Photo: analyst working at monitors showing code in a dim office"/>
    </svg>
    <div class="cover-brand">
      <span class="cover-brand__mark"></span>
      <div class="cover-brand__name">BRANKELL</div>
      <div class="cover-brand__sub">ADVISORY</div>
    </div>
    <h1 class="cover-title">Innovative EPM Solutions<br>for Finance and Beyond</h1>
    <div class="tab tab--blue">1</div>
  </section>

  <!-- 2 agenda -->
  <section class="slide slide--agenda bg-blue" role="img" aria-label="Background: abstract blue digital network">
    <svg class="shapes" viewBox="0 0 576 324" preserveAspectRatio="none">
      <polygon points="0,0 92,0 92,71 0,117" fill="#fff"/>
    </svg>
    <div class="brand"><span class="brand__mark"></span><div class="brand__name">Brankell<br>Advisory</div></div>
    <h2 class="heading heading--white agenda-title">Agenda</h2>
    <table class="agenda-table">
      <tr><th>PG. NO</th><th>CONTENT</th></tr>
      <tr><td class="pg">01</td><td>Aliquam erat volutpat</td></tr>
      <tr><td class="pg">02</td><td>Quisque aliquet ex nec est vestibulum pulvinar</td></tr>
      <tr><td class="pg">03</td><td>Pellentesque convallis molestie enim sit amet efficitur</td></tr>
      <tr><td class="pg">04</td><td>Etiam id imperdiet lectus</td></tr>
      <tr><td class="pg">05</td><td>Vivamus lacus justo, ultrices nec erat in, euismod iaculis mauris</td></tr>
      <tr><td class="pg">06</td><td>Vivamus eleifend vitae nulla vel malesuada</td></tr>
      <tr><td class="pg">07</td><td>Aenean placerat, nibh vel accumsan aliquet, magna nibh accumsan nibh, ac tempus nunc ipsum ac tellus</td></tr>
      <tr><td class="pg">08</td><td>Cras augue magna, placerat eget nulla non, congue suscipit neque</td></tr>
      <tr><td class="pg">09</td><td>Vestibulum ante ipsum primis in faucibus orci luctus et ultrices posuere cubilia</td></tr>
      <tr><td class="pg">10</td><td>Phasellus nisl est, condimentum vitae faucibus in, sollicitudin vel metus</td></tr>
    </table>
    <div class="tab">2</div>
  </section>

  <!-- 3 section -->
  <section class="slide slide--section">
    <svg class="shapes" viewBox="0 0 576 324" preserveAspectRatio="none">
      <defs>
        <linearGradient id="sectionPhoto" x1="0" y1="0" x2="0" y2="1">
          <stop offset="0" stop-color="#c9a7b4"/>
          <stop offset=".45" stop-color="#5a5a7c"/>
          <stop offset="1" stop-color="#163a6e"/>
        </linearGradient>
      </defs>
      <polygon points="0,0 281,0 281,157 0,324" fill="url(#sectionPhoto)" role="img" aria-label="Photo: silhouetted business people over a blue network"/>
      <polygon points="0,0 92,0 92,71 0,117" fill="#fff"/>
    </svg>
    <div class="brand"><span class="brand__mark"></span><div class="brand__name">Brankell<br>Advisory</div></div>
    <h2 class="heading heading--blue" style="left:310px;top:26px">Nunc sit amet<br>consequat risus</h2>
    <div class="body-copy" style="left:310px;top:84px;width:230px">
      <p>Aenean sed quam non sapien faucibus consequat vitae sit amet orci. Praesent quis risus mi. In mollis nulla in pulvinar dictum. Vivamus interdum sagittis felis, ut dapibus ligula feugiat ac. In dictum sapien eu tellus finibus fermentum. Aenean faucibus lacus ut mollis commodo. Donec vestibulum odio sem, ac laoreet massa ullamcorper id.</p>
      <p>Donec molestie nisi et tellus hendrerit vehicula. Nunc eu ligula sed quam pulvinar maximus in vitae eros. Proin porta fermentum ipsum, vel porttitor turpis venenatis luctus. Vivamus volutpat eu sapien quis tempus. Aenean feugiat viverra lorem ac sagittis. Donec sit amet lectus nec mi tempor auctor sapien.</p>
      <p>Nullam accumsan purus vel tempus viverra. Mauris suscipit felis id nunc elementum varius. Praesent elementum nulla sit amet justo pellentesque scelerisque. Nam et tortor in ante iaculis porttitor in luctus mi. Vivamus gravida sem a pretium euismod. Nam lobortis, purus et fringilla tempus, risus eros dignissim diam, eget finibus sem risus sit amet eros. Vestibulum facilisis dolor at purus tincidunt porta. Nam fringilla nulla vel nisl condimentum, dapibus condimentum enim porta. Phasellus blandit quam a ipsum gravida dapibus.</p>
    </div>
    <div class="tab">3</div>
  </section>

  <!-- 4 bullets -->
  <section class="slide slide--bullets bg-blue">
    <svg class="shapes" viewBox="0 0 576 324" preserveAspectRatio="none">
      <defs>
        <linearGradient id="bulletPhoto" x1="0" y1="0" x2="1" y2="1">
          <stop offset="0" stop-color="#9fb3c4"/>
          <stop offset=".5" stop-color="#7fd0f2"/>
          <stop offset="1" stop-color="#6f7c88"/>
        </linearGradient>
      </defs>
      <polygon points="294,0 576,0 576,324 294,190" fill="url(#bulletPhoto)" role="img" aria-label="Photo: person typing on a laptop beneath a cloud network graphic"/>
      <polygon points="0,0 92,0 92,66 0,118" fill="#fff"/>
    </svg>
    <div class="brand"><span class="brand__mark"></span><div class="brand__name">Brankell<br>Advisory</div></div>
    <h2 class="heading heading--white" style="left:6px;top:124px">Suspendisse elit<br>iaculis ea dignissim</h2>
    <ul class="bullets bullets--white" style="left:6px;top:183px">
      <li>Aliquam ac elit vitae sapien elementum pulvinar eu eget leo.</li>
      <li>Nulla ut neque mattis, ornare ipsum pellentesque, volutpat purus.</li>
      <li>Nam ultrices orci nec odio tincidunt dignissim.</li>
      <li>Proin ut enim blandit, egestas libero a, congue odio.</li>
      <li>Donec aliquam quam eget euismod dictum.</li>
      <li>In pulvinar nibh non velit maximus semper.</li>
      <li>Nunc pellentesque diam at lacus pellentesque blandit.</li>
    </ul>
    <div class="tab">4</div>
  </section>

  <!-- 5 subtitle + bullets -->
  <section class="slide slide--subtitle">
    <svg class="shapes" viewBox="0 0 576 324" preserveAspectRatio="none">
      <defs>
        <linearGradient id="subPhoto" x1="0" y1="0" x2="1" y2="1">
          <stop offset="0" stop-color="#d8d6d0"/>
          <stop offset=".5" stop-color="#8a97ad"/>
          <stop offset="1" stop-color="#4a4f5a"/>
        </linearGradient>
      </defs>
      <polygon points="0,0 281,0 281,166 0,324" fill="url(#subPhoto)" role="img" aria-label="Photo: technician installing a server in a data centre rack"/>
      <polygon points="0,0 92,0 92,66 0,118" fill="#fff"/>
    </svg>
    <div class="brand"><span class="brand__mark"></span><div class="brand__name">Brankell<br>Advisory</div></div>
    <h2 class="heading heading--blue" style="left:310px;top:29px">Aliquam dignissim</h2>
    <p class="subtitle" style="left:310px;top:62px;width:250px">Nam tempus augue eu ante lacinia, euismod sodales ligula porttitor feugiat rhoncus quis.</p>
    <ul class="bullets bullets--dark" style="left:310px;top:105px">
      <li>Aliquam ac elit vitae sapien elementum pulvinar eu eget leo.</li>
      <li>Nulla ut neque mattis, ornare ipsum pellentesque, volutpat purus.</li>
      <li>Nam ultrices orci nec odio tincidunt dignissim.</li>
      <li>Proin ut enim blandit, egestas libero a, congue odio.</li>
      <li>Donec aliquam quam eget euismod dictum.</li>
      <li>In pulvinar nibh non velit maximus semper.</li>
      <li>Nunc pellentesque diam at lacus pellentesque blandit.</li>
      <li>Maecenas sed nibh sed nisi tristique pharetra.</li>
      <li>Vestibulum ut velit elementum, bibendum neque</li>
      <li>Quisque blandit elit at urna tincidunt, sed laoreet odio consequat.</li>
    </ul>
    <div class="tab">5</div>
  </section>

  <!-- 6 two columns -->
  <section class="slide slide--columns bg-blue">
    <svg class="shapes" viewBox="0 0 576 324" preserveAspectRatio="none">
      <polygon points="0,0 92,0 92,66 0,118" fill="#fff"/>
    </svg>
    <div class="brand"><span class="brand__mark"></span><div class="brand__name">Brankell<br>Advisory</div></div>
    <h2 class="heading heading--white" style="left:92px;width:390px;text-align:center;top:42px;line-height:27px">Duis quam auctor<br>dapibus justo commodo</h2>
    <div class="column" style="left:6px">
      <p>Mauris quis sodales enim, semper ultricies massa. Pellentesque risus dolor, tristique vel facilisis at, laoreet ut elit. Fusce id augue at metus cursus pulvinar. In nec lectus porttitor, porttitor velit vel, tempus tortor. Duis sed suscipit leo, ut dictum nulla. Maecenas id malesuada ex. Curabitur a sem ut ex sollicitudin fringilla. Aenean fringilla ante non tincidunt posuere. Cras sollicitudin lectus vel enim placerat rhoncus. Curabitur sed dui feugiat, ultricies mi vitae, molestie nulla. Class aptent taciti sociosqu ad litora torquent per conubia nostra, per inceptos himenaeos.</p>
      <p>Suspendisse potenti. Suspendisse feugiat purus metus, nec interdum elit dignissim eget. Pellentesque habitant morbi tristique senectus et netus et malesuada fames ac turpis egestas.</p>
    </div>
    <div class="column" style="left:302px">
      <p>Aliquam sed felis dui. Ut luctus ut eros malesuada blandit. Praesent scelerisque fermentum mauris ut posuere. Curabitur non risus sed ante rhoncus semper. Praesent blandit, neque at porta sodales, ex diam tempus mi, eu fringilla odio leo at diam.</p>
      <p>Nam id enim dictum, pretium nisi et, porta libero. Fusce sodales, odio eget egestas faucibus, ex dolor lacinia diam, condimentum maximus felis nulla ut metus. Suspendisse dapibus eros massa, ac iaculis ipsum venenatis sed. Pellentesque scelerisque auctor erat, at faucibus enim sollicitudin condimentum. Suspendisse eu enim ut lectus cursus commodo aliquet porta eros. Aenean tortor metus, venenatis eu luctus et, aliquet at tortor. Morbi at lectus est. Donec eu erat id purus lobortis lobortis.</p>
    </div>
    <div class="tab">6</div>
  </section>

</div>
</body>
</html>
```